Beacon Advisory Website

I currently have a website www.beaconadvisoryinc.example. We are a IT Consulting Company. Our website will pretty much tell out our services. I am looking to enhance my website and make it look more professional. Looking for very classy and Contemporary look and design for my website.

Industry/Entity Type

It Company

```html
<!DOCTYPE html>
<html lang="en">
<head>
<meta charset="utf-8">
<title>Beacon Advisory</title>
<link rel="stylesheet" href="https://fonts.googleapis.com/css2?family=Josefin+Sans:wght@400;600;700&family=Open+Sans:wght@400;600;700&display=swap">
<style>
:root{
  --blue:#1c5ea8;
  --blue-dark:#174f8f;
  --sky:#1a8fc4;
  --navy:#0f2744;
  --ink:#1e1e1e;
  --muted:#8a8a8a;
  --red:#e8473f;
  --grey-band:#f1f0f0;
  --gold:#d39538;
  --rose:#a64660;
  --slate:#35416b;
  --white:#ffffff;
  --head:"Josefin Sans", sans-serif;
  --body:"Open Sans", sans-serif;
}
*{margin:0;padding:0;box-sizing:border-box}
html,body{width:1200px;height:2866px;overflow:hidden;background:var(--white)}
body{position:relative;font-family:var(--body);color:var(--ink)}
.abs{position:absolute}
.center{text-align:center;left:0;width:1200px}

/* header */
.brand{left:162px;top:30px;display:flex;align-items:center;gap:10px}
.brand-mark{width:34px;height:34px;background:var(--sky);border-radius:4px}
.brand-name{font-family:var(--head);font-weight:700;font-size:21px;color:var(--blue);line-height:1}
.main-nav{top:40px;right:159px;display:flex;align-items:center;gap:22px}
.main-nav a{font-family:var(--head);font-weight:700;font-size:12px;color:var(--blue);text-decoration:none;letter-spacing:.5px}
.home-icon{width:26px;height:26px}

/* hero */
.hero{top:100px;left:0;width:1200px;height:460px;
  background:linear-gradient(180deg,#c9b79a 0%,#a68f73 30%,#5f5d60 60%,#2f3844 100%)}
.hero-title{top:328px;font-family:var(--head);font-weight:600;font-size:34px;letter-spacing:5px;color:var(--white)}
.hero-dots{top:506px;left:558px;display:flex;gap:8px}
.hero-dots span{width:24px;height:4px;background:rgba(255,255,255,.5)}
.hero-dots span.on{background:#f3c42c}

/* about */
.about{top:560px;left:0;width:1200px;height:230px;background:var(--grey-band)}
.section-title{font-family:var(--head);font-weight:700;font-size:17px;letter-spacing:2px;color:var(--ink)}
.about .section-title{top:40px}
.about-text{left:239px;top:70px;width:722px;text-align:center;font-size:12.3px;line-height:24px;color:#2a2a2a}
.next-btn{top:772px;left:582px;width:36px;height:36px}

/* provide */
.blue-title{font-family:var(--head);font-weight:700;font-size:19px;letter-spacing:2px;color:var(--blue)}
.subtitle{font-family:var(--head);font-size:13px;letter-spacing:1.5px;color:#333}
.services{top:930px;left:160px;width:880px;height:327px;background:var(--blue);display:flex}
.service{flex:1;border-right:1px solid rgba(255,255,255,.12);text-align:center;color:var(--white);padding:58px 14px 0;position:relative}
.service:last-child{border-right:none}
.service svg.icon{width:44px;height:44px}
.service h3{font-family:var(--head);font-weight:700;font-size:12px;letter-spacing:.5px;margin-top:18px}
.service p{font-size:10.5px;line-height:19px;height:95px;overflow:hidden;margin:14px auto 0;width:130px}
.service .more{position:absolute;left:50%;bottom:22px;transform:translateX(-50%);width:26px;height:12px}

/* band */
.band{top:1317px;left:0;width:1200px;height:183px;
  background:linear-gradient(180deg,#6d7378 0%,#8f9296 40%,#6b6a69 70%,#3f4448 100%)}
.band-title{top:1384px;font-family:var(--head);font-weight:600;font-size:22px;letter-spacing:5px;line-height:22px;color:var(--white)}

/* pride */
.stat{width:220px;text-align:center;top:1672px}
.stat svg{width:40px;height:40px;display:block;margin:0 auto}
.stat .num{font-family:var(--head);font-weight:600;font-size:44px;color:var(--red);line-height:1;margin-top:18px}
.stat .label{font-family:var(--body);font-weight:700;font-size:15px;margin-top:2px}
.stat p{font-size:10px;line-height:19px;color:var(--muted);margin-top:6px}

/* solutions */
.solutions-main{top:1928px;left:160px;width:385px;height:142px;background:var(--sky);color:var(--white);display:flex;align-items:center;justify-content:center;font-family:var(--head);font-weight:600;font-size:21px;letter-spacing:4px}
.tile{display:flex;align-items:center;justify-content:center;color:var(--white);font-family:var(--head);font-weight:600;font-size:15px;letter-spacing:3px}
.tile-gold{top:1928px;left:547px;width:244px;height:69px;background:var(--gold)}
.tile-rose{top:1928px;left:795px;width:245px;height:69px;background:var(--rose)}
.tile-slate{top:2001px;left:547px;width:493px;height:69px;background:var(--slate)}

/* testimonials */
.avatar{top:2246px;left:229px;width:76px;height:76px;border-radius:50%;background:linear-gradient(180deg,#d9d9d9,#7c7c7c)}
.quote-name{top:2244px;left:328px;font-size:13px;color:var(--muted)}
.quote-text{top:2272px;left:328px;width:660px;font-size:11.5px;line-height:23px;color:#333}
.dots{top:2358px;left:581px;display:flex;gap:7px}
.dots span{width:8px;height:8px;border-radius:50%;background:#c9c9c9}
.dots span.on{background:var(--sky)}

/* partners */
.partners{top:2431px;left:0;width:1200px;height:149px;background:var(--grey-band)}
.badge{background:#1e1e1e}

/* footer */
.site-footer{top:2580px;left:0;width:1200px;height:286px;background:var(--navy)}
.foot-brand{left:162px;top:2628px;display:flex;align-items:center;gap:10px}
.foot-brand .brand-name{color:var(--sky)}
.foot-nav{top:2633px;left:480px;display:flex;gap:22px}
.foot-nav a{font-family:var(--head);font-weight:600;font-size:11px;color:var(--sky);text-decoration:none;letter-spacing:.5px}
.office{top:2678px;color:var(--white);font-family:var(--head);font-size:11.5px;line-height:23px;letter-spacing:.3px}
.office h4{font-weight:700;font-size:11.5px}
.copyright{top:2808px;left:160px;font-family:var(--head);font-size:9.5px;color:#b9c3cf;letter-spacing:.3px}
.phone{top:2803px;left:480px;font-family:var(--head);font-weight:600;font-size:16px;color:var(--sky);letter-spacing:.5px}
.social{top:2801px;left:938px;display:flex;gap:15px}
.social span{width:24px;height:24px;border-radius:50%;background:var(--white)}
</style>
</head>
<body>

<header>
  <div class="abs brand"><span class="brand-mark"></span><span class="brand-name">Beacon Advisory</span></div>
  <nav class="abs main-nav">
    <svg class="home-icon" viewBox="0 0 26 26" aria-label="Home"><circle cx="13" cy="13" r="13" fill="#1c5ea8"/><path d="M7 13.5 13 8l6 5.5h-2V19h-3v-3.5h-2V19H9v-5.5z" fill="#fff"/></svg>
    <a href="#">COMPANY</a><a href="#">SERVICES</a><a href="#">SOLUTIONS</a><a href="#">RESOURCES</a><a href="#">CAREER</a><a href="#">CONTACT</a>
  </nav>
</header>

<section>
  <div class="abs hero" role="img" aria-label="Aerial photograph of a city skyline with skyscrapers at sunset"></div>
  <h1 class="abs center hero-title">MAINTAINING GLOBAL PRESENCE</h1>
  <div class="abs hero-dots"><span></span><span class="on"></span><span></span></div>
</section>

<section class="abs about">
  <h2 class="abs center section-title">ABOUT OUR COMPANY</h2>
  <p class="abs about-text">Today's IT market is a dynamic, fast-paced industry, with ever-increasing demands. Meeting these demands for over 25 years, Beacon Advisory maintains a global presence, aggressively recruiting expertly qualified IT and Management Professionals from around the world and cultivating key partnerships with corporations to understand their business models end-to-end, with a goal of delivering exceptional client service and ensuring a consistent delivery of the talent needed to drive results.</p>
</section>
<svg class="abs next-btn" viewBox="0 0 36 36" aria-label="Next"><circle cx="18" cy="18" r="17" fill="#1e1e1e"/><circle cx="18" cy="18" r="11" fill="none" stroke="#fff" stroke-width="2"/><path d="M16 13l5 5-5 5" fill="none" stroke="#fff" stroke-width="2.4"/></svg>

<section>
  <h2 class="abs center blue-title" style="top:856px">WE PROVIDE</h2>
  <p class="abs center subtitle" style="top:886px">DELIVERING SERVICES THAT COMBINE QUALITY, RELIABILITY AND COMPLIANCE!</p>
  <div class="abs services">
    <div class="service">
      <svg class="icon" viewBox="0 0 44 44" fill="none" stroke="#fff" stroke-width="2.5"><rect x="11" y="11" width="22" height="22" rx="2"/><rect x="17" y="17" width="10" height="10" fill="#fff"/><path d="M16 5v6M22 5v6M28 5v6M16 33v6M22 33v6M28 33v6M5 16h6M5 22h6M5 28h6M33 16h6M33 22h6M33 28h6"/></svg>
      <h3>TECHNOLOGY</h3>
      <p>We are successful in deploying all students we trained into project with 2-3 weeks after training program. Our training programs will last for 6-8 weeks.</p>
      <svg class="more" viewBox="0 0 26 12" fill="none" stroke="#fff" stroke-width="2"><path d="M1 6h3M7 6h3M13 6h10M19 2l4 4-4 4"/></svg>
    </div>
    <div class="service">
      <svg class="icon" viewBox="0 0 44 44"><rect x="16" y="7" width="12" height="7" rx="2" fill="none" stroke="#fff" stroke-width="2.5"/><rect x="5" y="13" width="34" height="24" rx="2" fill="#fff"/><rect x="19" y="22" width="6" height="5" fill="#1c5ea8"/></svg>
      <h3>BUSINESS</h3>
      <p>Our Offshore Development Center at Hyderabad, India is comprised of an excellent delivery facility and staff dedicated to our customer's IT requirements.</p>
      <svg class="more" viewBox="0 0 26 12" fill="none" stroke="#fff" stroke-width="2"><path d="M1 6h3M7 6h3M13 6h10M19 2l4 4-4 4"/></svg>
    </div>
    <div class="service">
      <svg class="icon" viewBox="0 0 44 44" fill="none" stroke="#fff" stroke-width="2.5"><rect x="5" y="7" width="34" height="24" rx="2"/><path d="M17 38h10M22 31v7"/><circle cx="22" cy="19" r="5" fill="#fff"/></svg>
      <h3>APPLICATION DEV</h3>
      <p>The Beacon Advisory Website Design team creates professional, High-Quality, good Looking and thought-provoking Web sites that stand out from the rest.</p>
      <svg class="more" viewBox="0 0 26 12" fill="none" stroke="#fff" stroke-width="2"><path d="M1 6h3M7 6h3M13 6h10M19 2l4 4-4 4"/></svg>
    </div>
    <div class="service">
      <svg class="icon" viewBox="0 0 44 44" fill="#fff"><path d="M22 5 39 13 22 21 5 13z"/><path d="M5 20l17 8 17-8v4l-17 8-17-8z"/><path d="M5 29l17 8 17-8v4l-17 8-17-8z"/></svg>
      <h3>ENTERPRISE INTEGRATION</h3>
      <p>The IT landscape has seen an explosive rate of growth over the past several years. However, simply throwing technology at a business problem rarely works.</p>
      <svg class="more" viewBox="0 0 26 12" fill="none" stroke="#fff" stroke-width="2"><path d="M1 6h3M7 6h3M13 6h10M19 2l4 4-4 4"/></svg>
    </div>
    <div class="service">
      <svg class="icon" viewBox="0 0 44 44" fill="#fff"><circle cx="17" cy="13" r="6"/><path d="M5 36c0-8 5-13 12-13s12 5 12 13z"/><circle cx="32" cy="28" r="7" fill="none" stroke="#fff" stroke-width="2.5"/><path d="M29 28h6M32 25v6" stroke="#fff" stroke-width="2"/></svg>
      <h3>IT CONSULTING</h3>
      <p>Information technology should improve business results. Northgate helps companies make sure it does. We look at IT issues strategically, in the broader context.</p>
      <svg class="more" viewBox="0 0 26 12" fill="none" stroke="#fff" stroke-width="2"><path d="M1 6h3M7 6h3M13 6h10M19 2l4 4-4 4"/></svg>
    </div>
  </div>
</section>

<section>
  <div class="abs band" role="img" aria-label="Photograph of a suspension bridge rising out of fog over the hills"></div>
  <h2 class="abs center band-title">BEST PROFESSIONAL CONSULTING<br>AT YOUR SERVICE</h2>
</section>

<section>
  <h2 class="abs center blue-title" style="top:1545px">OUR PRIDE</h2>
  <p class="abs center subtitle" style="top:1585px;line-height:23px">OUR RESULTS BECOME OUR REPUTATION — AND SO IT IS A MATTER OF PERSONAL PRIDE<br>THAT WE DO EVERYTHING WE CAN TO GROW YOUR BUSINESS</p>

  <div class="abs stat" style="left:152px">
    <svg viewBox="0 0 40 40" fill="none" stroke="#9a9a9a" stroke-width="2"><path d="M4 14 11 6h18l7 8-16 20z"/><path d="M4 14h32M15 6l-4 8 9 20 9-20-4-8"/></svg>
    <div class="num">67</div><div class="label">Clients</div>
    <p>Kestrelwood clients share our passion for results and it is shown in their success. Companies that outperform the market like to work with us. Learn more by reading from our ...</p>
  </div>
  <div class="abs stat" style="left:377px">
    <svg viewBox="0 0 40 40" fill="none" stroke="#9a9a9a" stroke-width="2"><circle cx="20" cy="20" r="16"/><ellipse cx="20" cy="20" rx="7" ry="16"/><path d="M4 20h32M7 12h26M7 28h26"/></svg>
    <div class="num">16</div><div class="label">Countries</div>
    <p>Kestrelwood is a global business network of more than 21,000 companies that deliver innovative business solutions. Through access to our company's premier products</p>
  </div>
  <div class="abs stat" style="left:601px">
    <svg viewBox="0 0 40 40" fill="none" stroke="#9a9a9a" stroke-width="2"><path d="M34 6c-10 0-17 6-21 16l6 6c10-4 16-11 15-22z"/><circle cx="25" cy="15" r="3"/><path d="M13 22H7l5-6h6M19 28v6l6-5v-6M11 30l-5 5"/></svg>
    <div class="num">457</div><div class="label">Projects</div>
    <p>Kestrelwood projects give enterprises the opportunity to extend and reevaluate their current business strategy from a fresh point of view or to find a solution for a topic ...</p>
  </div>
  <div class="abs stat" style="left:826px">
    <svg viewBox="0 0 40 40" fill="none" stroke="#9a9a9a" stroke-width="2"><circle cx="20" cy="13" r="8"/><path d="M5 37c0-9 6-14 15-14s15 5 15 14z"/></svg>
    <div class="num">56</div><div class="label">People in Staff</div>
    <p>Although we're proud of our products, services, and technology, nothing matches the pride we have in our staff. We are committed to providing excellent customer ...</p>
  </div>
</section>

<section>
  <div class="abs solutions-main">OUR SOLUTIONS</div>
  <div class="abs tile tile-gold">DASHBOARD</div>
  <div class="abs tile tile-rose">BPM</div>
  <div class="abs tile tile-slate">DATA WAREHOUSING</div>
</section>

<section>
  <h2 class="abs center section-title" style="top:2153px">TESTIMONIALS</h2>
  <p class="abs center subtitle" style="top:2181px">HAVE A LOOK AT SOME OF OUR CLIENT'S TESTIMONIALS AS WELL AS WHAT SOME OF THE SUPPLIERS SAY</p>
  <div class="abs avatar" role="img" aria-label="Portrait photo of the client giving the testimonial"></div>
  <div class="abs quote-name">Daniel Whitmore</div>
  <p class="abs quote-text">Lorem ipsum dolor sit amet, consectetur adipiscing elit. Nulla varius tincidunt libero, vel fermentum turpis posuere ac. Etiam eleifend enim eleifend dolor bibendum, mollis sodales lectus vulputate. Nunc elit nisl...</p>
  <div class="abs dots"><span class="on"></span><span></span><span></span></div>
</section>

<section class="abs partners" aria-label="Partners">
  <div class="abs badge" style="left:222px;top:40px;width:68px;height:68px;border-radius:50%;background:none;border:3px solid #1e1e1e"></div>
  <div class="abs badge" style="left:432px;top:36px;width:76px;height:76px;border-radius:50%"></div>
  <div class="abs badge" style="left:658px;top:50px;width:110px;height:48px"></div>
  <div class="abs badge" style="left:903px;top:40px;width:86px;height:68px;border-radius:14px"></div>
</section>

<footer class="abs site-footer"></footer>
<div class="abs foot-brand"><span class="brand-mark"></span><span class="brand-name">Beacon Advisory</span></div>
<nav class="abs foot-nav"><a href="#">COMPANY</a><a href="#">SERVICES</a><a href="#">SOLUTIONS</a><a href="#">RESOURCES</a><a href="#">CAREER</a><a href="#">CONTACT</a></nav>
<div class="abs office" style="left:480px"><h4>HEAD OFFICE</h4>412 ALDER AVE<br>SUITE 110<br>MAPLE RIDGE, NJ 07000</div>
<div class="abs office" style="left:705px"><h4>TECHNICAL CENTER</h4>2750 CEDAR LINE ROAD<br>SUITE 300<br>OAKVIEW HILLS MI 48000</div>
<div class="abs office" style="left:925px"><h4>WEST COAST OFFICE</h4>1880 HARBOR POINT WAY<br>SUITE 410<br>BAYFIELD, CA 95000</div>
<div class="abs copyright">© 2016, BEACON ADVISORY</div>
<div class="abs phone">PHONE: +1 (555) 014 2290</div>
<div class="abs social" aria-label="Social links"><span></span><span></span><span></span></div>

</body>
</html>
```